Harborline Telecom Print Ad

I'm looking for a four panel piece for Harborline Telecom similar to the attached ad for QuietEar that is a clean, not too busy look using the elements from Harborline Telecom's website:

https://www.harborlinetelecom.example/

We like to include impactful imagery on the cover, more details on the service like a quote from their Founder, a "How it works" section, and other simple icons to communicate Harborline Telecom's benefits in the middle two panels, and testimonials on the back.

Here are a few other 4 panel creative examples for creative inspiration:

https://pages.leafviewer.example/view/471903586/

```html
<!DOCTYPE html>
<html lang="en">
<head>
<meta charset="utf-8">
<title>Harborline Telecom – Four Panel Print Ad</title>
<link href="https://fonts.googleapis.com/css2?family=Montserrat:wght@400;500;600;700&display=swap" rel="stylesheet">
<style>
:root{
  --purple:#7b6cf0;
  --ink:#14172b;
  --muted:#6a6f80;
  --body:#3b3f4c;
  --panel-bg:#e1f8fc;
  --band:#c4f0fb;
  --cover-bg:#d5eaf2;
  --card:#ffffff;
  --star-green:#1aa564;
  --star-navy:#1b4d80;
  --star-red:#e8473b;
  --star-gold:#f5b400;
  --client:#2f8fe0;
}
*{box-sizing:border-box;margin:0;padding:0}
html,body{width:928px;height:1200px;overflow:hidden;background:#fff}
body{font-family:"Montserrat",sans-serif;color:var(--ink);position:relative}
.panel{position:absolute;width:443px;height:573px;overflow:hidden}
.cover{left:12px;top:7px;background:var(--cover-bg)}
.founder{left:463px;top:7px;background:var(--panel-bg)}
.benefits{left:12px;top:595px;background:var(--panel-bg)}
.reviews{left:466px;top:595px;background:var(--panel-bg)}
.abs{position:absolute}
.photo{position:absolute}

/* cover */
.cover .photo{inset:0;background:linear-gradient(150deg,#9aa3a8 0%,#5d5f60 35%,#2a2b2d 65%,#8b7a66 100%);clip-path:polygon(100% 0,100% 100%,0 100%,0 78%)}
.brand{left:12px;top:44px;font-size:19px;font-weight:700;letter-spacing:.3px}
.brand-dot{display:inline-block;width:7px;height:7px;border-radius:50%;background:var(--purple);margin-right:5px;vertical-align:middle}
.cover-headline{left:12px;top:88px;font-size:16px;font-weight:400;line-height:19px}
.cover-headline strong{color:var(--purple);font-weight:600}
.partners{left:11px;top:158px;display:grid;grid-template-columns:68px 80px;row-gap:20px;column-gap:0}
.partner{font-size:9px;font-weight:700;line-height:11px;color:var(--ink);height:34px;display:flex;align-items:center}

/* shared */
.h-purple{color:var(--purple);font-weight:700}
.card{position:absolute;background:var(--card);box-shadow:0 1px 4px rgba(0,0,0,.12);border-bottom:2px solid var(--purple)}
.icon-badge{position:absolute;width:42px;height:42px;border-radius:50%;background:#fff;box-shadow:0 2px 5px rgba(0,0,0,.18);display:flex;align-items:center;justify-content:center}
.card-title{font-size:9px;font-weight:700;line-height:12px}
.card-text{font-size:6px;color:var(--muted);line-height:11px}

/* founder */
.founder-title{left:14px;top:18px;font-size:16.5px}
.founder .portrait{left:18px;top:52px;width:145px;height:164px;border-radius:4px;background:linear-gradient(160deg,#e6e8ea,#b7bcc0 60%,#39485a)}
.letter{left:181px;top:52px;width:220px;font-size:6.4px;line-height:10.8px;color:var(--body)}
.sign-name{left:181px;top:196px;font-size:8px;font-weight:700;color:var(--purple)}
.sign-role{left:181px;top:209px;font-size:6.4px;color:var(--body)}
.how-title{left:168px;top:232px;font-size:16.5px}
.step{padding:0 7px}
.step .card-title{margin-top:33px}
.step .card-text{margin-top:7px}
.reliable-title{left:14px;top:408px;font-size:15.5px;line-height:19px}
.reliable-sub{left:14px;top:453px;font-size:9px;line-height:12.5px;width:270px;color:var(--body)}
.feature{position:absolute;font-size:6.5px;line-height:10.8px;color:var(--body);padding-left:11px}
.feature svg{position:absolute;left:0;top:0}
.founder .caller{left:322px;top:405px;width:121px;height:168px;background:linear-gradient(180deg,#e1f8fc 0%,#c9b6a4 35%,#f1efec 70%)}

/* benefits */
.benefits-title{left:11px;top:34px;font-size:16px;line-height:19.5px}
.benefit{width:126px;height:108px;padding:0 7px}
.benefit .card-title{margin-top:34px}
.benefit .card-text{margin-top:6px}
.benefits .elder{left:286px;top:0;width:157px;height:573px;background:linear-gradient(180deg,#b6b1dd 0%,#cdbfc8 35%,#3e4a7a 70%,#4f5c8c 100%)}

/* reviews */
.reviews .band{left:0;top:0;width:443px;height:94px;background:var(--band)}
.reviews-title{left:16px;top:30px;font-size:16.5px;line-height:21px}
.rating{width:127px;height:60px;text-align:center;border-bottom:none}
.rating-name{margin-top:10px;font-size:12px;font-weight:600;height:18px;display:flex;align-items:center;justify-content:center;gap:4px}
.rating-score{margin-top:4px;font-size:11px;font-weight:600;letter-spacing:1px}
.badge-shape{width:44px;height:16px;background:var(--star-navy);border-radius:2px}
.review{width:131px;height:156px;text-align:center;padding:0 6px;border-bottom:none;box-shadow:0 0 0 1px #e3e6ea}
.avatar{width:46px;height:46px;border-radius:50%;margin:9px auto 0;background:linear-gradient(180deg,#dcdfe2,#a9b0b8)}
.rev-name{margin-top:6px;font-size:7px;font-weight:600}
.rev-role{font-size:6px;color:var(--client);margin-top:1px}
.rev-text{font-size:5.8px;line-height:10.7px;color:var(--muted);margin-top:4px;position:relative}
.rev-text::before{content:"\201C";position:absolute;left:-1px;top:-6px;font-size:9px;color:var(--ink);font-weight:700}
.rev-stars{font-size:8px;color:var(--star-gold);letter-spacing:.5px;margin-top:1px}
</style>
</head>
<body>

<section class="panel cover">
  <div class="photo" role="img" aria-label="Close-up of a hand dialing a black desk phone on an office table"></div>
  <div class="abs brand"><span class="brand-dot"></span>harborline telecom</div>
  <h1 class="abs cover-headline">Simple, reliable, phone<br>service for Home,<br><strong>Business</strong></h1>
  <div class="abs partners">
    <div class="partner">Crumbly Cafe</div>
    <div class="partner">Greenleaf Roasters</div>
    <div class="partner">Ridgeway Bank</div>
    <div class="partner">Hen House Grill</div>
    <div class="partner">Northfuel</div>
    <div class="partner">Fizzwell</div>
  </div>
</section>

<section class="panel founder">
  <h2 class="abs h-purple founder-title">We fight to keep the landline alive</h2>
  <div class="photo portrait" role="img" aria-label="Portrait of the founder in glasses and a dark polo shirt"></div>
  <p class="abs letter">I started Harborline Telecom to build a different kind of landline phone service company.<br>
  We don’t nickel and dime you with hidden fees. We make it easy for you to actually reach a real person when you have a problem.<br>
  We don’t tie you up in long contracts, or discontinue your service when it’s no longer “profitable” to serve you with copper wire service. And we don’t require you to have fast, reliable internet, just to make a call.<br>
  I built Harborline Telecom to make it easy, safe, and reliable to stay connected with your family and friends.<br>
  If that sounds like what you’re looking for from your landline phone company, then you’re at the right place. We’d love to have you as part of the Harborline family.</p>
  <div class="abs sign-name">Owen Hartley</div>
  <div class="abs sign-role">Founder &amp; CEO</div>

  <h2 class="abs h-purple how-title">How it works</h2>

  <div class="card step" style="left:16px;top:281px;width:126px;height:110px">
    <div class="card-title">Invite your friends</div>
    <p class="card-text">Tell your friends, family, and loved ones about Harborline Telecom. Refer as many as you want!</p>
  </div>
  <div class="icon-badge" style="left:21px;top:261px">
    <svg width="24" height="24" viewBox="0 0 24 24" fill="#7b6cf0"><circle cx="9" cy="7" r="4"/><path d="M1 20c0-5 4-7 8-7s6 1 7 3v4z"/><circle cx="18" cy="17" r="5" fill="#fff" stroke="#7b6cf0" stroke-width="1.5"/><path d="M18 14.5v5M15.5 17h5" stroke="#7b6cf0" stroke-width="1.5"/></svg>
  </div>

  <div class="card step" style="left:158px;top:281px;width:126px;height:110px">
    <div class="card-title">When they sign up</div>
    <p class="card-text">Have them mention the name on your Harborline Telecom account.</p>
  </div>
  <div class="icon-badge" style="left:164px;top:261px">
    <svg width="26" height="26" viewBox="0 0 24 24"><circle cx="12" cy="12" r="11" fill="#7b6cf0"/><path d="M12 18V6M7 11l5-5 5 5" stroke="#fff" stroke-width="2" fill="none" stroke-linecap="round"/></svg>
  </div>

  <div class="card step" style="left:301px;top:281px;width:126px;height:110px">
    <div class="card-title">After they sign up</div>
    <p class="card-text">You’ll get $50 off your next Harborline Telecom bill. The person you refer will get their first month of service absolutely FREE.</p>
  </div>
  <div class="icon-badge" style="left:306px;top:261px">
    <svg width="24" height="24" viewBox="0 0 24 24"><path d="M2 4h20v13H10l-4 4v-4H2z" fill="#7b6cf0"/><circle cx="10" cy="9" r="2" fill="#fff"/><path d="M6.5 14c0-2 2-3 3.5-3s3.5 1 3.5 3z" fill="#fff"/><path d="M16 8v4M14 10h4" stroke="#fff" stroke-width="1.5"/></svg>
  </div>

  <h2 class="abs h-purple reliable-title">Reliable Landline Phone Service<br>For Your Home</h2>
  <p class="abs reliable-sub">Home phone service that doesn’t require internet: the most reliable way to stay in touch with loved ones</p>
  <div class="feature" style="left:14px;top:494px"><svg width="10" height="10" viewBox="0 0 10 10"><path d="M1 5l3 3 5-7" stroke="#7b6cf0" stroke-width="1.8" fill="none"/></svg>Unlimited nationwide calling</div>
  <div class="feature" style="left:150px;top:494px"><svg width="10" height="10" viewBox="0 0 10 10"><path d="M1 5l3 3 5-7" stroke="#7b6cf0" stroke-width="1.8" fill="none"/></svg>30-second setup</div>
  <div class="feature" style="left:14px;top:513px"><svg width="10" height="10" viewBox="0 0 10 10"><path d="M1 5l3 3 5-7" stroke="#7b6cf0" stroke-width="1.8" fill="none"/></svg>Keep your existing number<br>(or get a new one)</div>
  <div class="feature" style="left:150px;top:513px"><svg width="10" height="10" viewBox="0 0 10 10"><path d="M1 5l3 3 5-7" stroke="#7b6cf0" stroke-width="1.8" fill="none"/></svg>Works without internet or<br>power</div>
  <div class="photo caller" role="img" aria-label="Smiling woman in a white shirt talking on a mobile phone"></div>
</section>

<section class="panel benefits">
  <h2 class="abs h-purple benefits-title">Landline phone service that<br>doesn't require the internet</h2>

  <div class="card benefit" style="left:9px;top:107px">
    <div class="card-title">No internet required</div>
    <p class="card-text">Don’t let the strength of your internet connection decide whether you can connect with your loved ones.</p>
  </div>
  <div class="icon-badge" style="left:16px;top:87px">
    <svg width="26" height="26" viewBox="0 0 24 24" fill="none" stroke="#7b6cf0" stroke-width="2.4" stroke-linecap="round"><path d="M2 9a14 14 0 0 1 20 0M5 13a9 9 0 0 1 14 0M8.5 16.5a4 4 0 0 1 7 0"/><circle cx="12" cy="20" r="1.2" fill="#7b6cf0"/><path d="M4 21L20 4"/></svg>
  </div>

  <div class="card benefit" style="left:152px;top:107px">
    <div class="card-title">Unlimited<br>nationwide calling</div>
    <p class="card-text">Stay in touch with loved ones anywhere in the United States with unlimited minutes.</p>
  </div>
  <div class="icon-badge" style="left:159px;top:87px">
    <svg width="24" height="24" viewBox="0 0 24 24"><path d="M5 3v19" stroke="#7b6cf0" stroke-width="2.4"/><path d="M6 3h13l-3 5 3 5H6z" fill="#7b6cf0"/></svg>
  </div>

  <div class="card benefit" style="left:9px;top:250px">
    <div class="card-title">Customer support you<br>can actually reach</div>
    <p class="card-text">Helpful, knowledgeable customer support you can reach via chat, email, or phone.</p>
  </div>
  <div class="icon-badge" style="left:16px;top:230px">
    <svg width="26" height="26" viewBox="0 0 24 24"><path d="M3 13v-2a9 9 0 0 1 18 0v2" stroke="#7b6cf0" stroke-width="2" fill="none"/><rect x="1.5" y="11" width="4" height="7" rx="1.5" fill="#7b6cf0"/><rect x="18.5" y="11" width="4" height="7" rx="1.5" fill="#7b6cf0"/><circle cx="12" cy="12" r="6" fill="#7b6cf0"/><circle cx="9.5" cy="12" r="1" fill="#fff"/><circle cx="12" cy="12" r="1" fill="#fff"/><circle cx="14.5" cy="12" r="1" fill="#fff"/></svg>
  </div>

  <div class="card benefit" style="left:152px;top:250px">
    <div class="card-title">Get a new, local<br>number</div>
    <p class="card-text">Or, keep your existing number by transferring it from your current provider.</p>
  </div>
  <div class="icon-badge" style="left:159px;top:230px">
    <svg width="24" height="24" viewBox="0 0 24 24"><path d="M2 8c0-3 4-5 10-5s10 2 10 5v2h-5V8H7v2H2z" fill="#7b6cf0"/><path d="M6 10h12l2 11H4z" fill="#7b6cf0"/><circle cx="12" cy="15" r="3" fill="#fff"/><circle cx="12" cy="15" r="1.3" fill="#7b6cf0"/></svg>
  </div>

  <div class="card benefit" style="left:9px;top:394px">
    <div class="card-title">30-second setup</div>
    <p class="card-text">You can set it up yourself — no technician required. All you need is a power outlet.</p>
  </div>
  <div class="icon-badge" style="left:16px;top:374px">
    <svg width="22" height="22" viewBox="0 0 24 24" fill="none" stroke="#7b6cf0" stroke-width="1.4"><rect x="4" y="2" width="16" height="20" rx="1"/><path d="M4 6h16M7 10h10M7 13h10M7 16h7"/></svg>
  </div>

  <div class="card benefit" style="left:152px;top:394px">
    <div class="card-title">Works during power<br>outages</div>
    <p class="card-text">Backup battery keeps you connected when the power goes out.</p>
  </div>
  <div class="icon-badge" style="left:159px;top:374px">
    <svg width="24" height="24" viewBox="0 0 24 24"><path d="M13 2L5 13h6l-1 9 8-11h-6z" fill="#7b6cf0"/><path d="M3 3l18 18" stroke="#7b6cf0" stroke-width="1.6"/></svg>
  </div>

  <div class="photo elder" role="img" aria-label="Older woman smiling while talking on a corded desk phone"></div>
</section>

<section class="panel reviews">
  <div class="abs band"></div>
  <h2 class="abs h-purple reviews-title">Harborline Telecom is rated the best home<br>phone service in the United States</h2>

  <div class="card rating" style="left:20px;top:111px">
    <div class="rating-name">ReviewNest</div>
    <div class="rating-score" style="color:var(--star-green)">4.5 ★★★★☆</div>
  </div>
  <div class="card rating" style="left:158px;top:111px">
    <div class="rating-name"><span class="badge-shape"></span></div>
    <div class="rating-score" style="color:var(--star-navy)">4.2 ★★★★☆</div>
  </div>
  <div class="card rating" style="left:297px;top:111px">
    <div class="rating-name">Searchly</div>
    <div class="rating-score" style="color:var(--star-red)">4.3 ★★★★☆</div>
  </div>

  <div class="card review" style="left:16px;top:190px">
    <div class="avatar" role="img" aria-label="Customer photo"></div>
    <div class="rev-name">Nora K</div><div class="rev-role">Client</div>
    <p class="rev-text">Placing our order for a home phone line was easy, and the equipment arrived in 3 days. We were up and running in no time, and service has been working perfectly!</p>
    <div class="rev-stars">★★★★★</div>
  </div>
  <div class="card review" style="left:155px;top:190px">
    <div class="avatar" role="img" aria-label="Customer photo"></div>
    <div class="rev-name">Theo B</div><div class="rev-role">Client</div>
    <p class="rev-text">Harborline Telecom’s landline phone service is outstanding! Clear calls and reliable connections. Highly recommended for hassle-free communication!</p>
    <div class="rev-stars">★★★★★</div>
  </div>
  <div class="card review" style="left:295px;top:190px">
    <div class="avatar" role="img" aria-label="Customer photo"></div>
    <div class="rev-name">Lena P</div><div class="rev-role">Client</div>
    <p class="rev-text">Excellent customer service. The only landline service near me that answered all questions with respect! Recommended the service to others, without hesitation.</p>
    <div class="rev-stars">★★★★★</div>
  </div>

  <div class="card review" style="left:16px;top:360px">
    <div class="avatar" role="img" aria-label="Customer photo"></div>
    <div class="rev-name">Marcus D</div><div class="rev-role">Client</div>
    <p class="rev-text">Got it for my mother. The home phone works without internet so she can call me or 911 when she needs to. Gives me peace of mind knowing she’s just a call away.</p>
    <div class="rev-stars">★★★★★</div>
  </div>
  <div class="card review" style="left:155px;top:360px">
    <div class="avatar" role="img" aria-label="Customer photo"></div>
    <div class="rev-name">Ivy R</div><div class="rev-role">Client</div>
    <p class="rev-text">I am very pleased with Harborline Telecom’s cheap landline service. From how nice their customer service agents were to how easy it was to set up.</p>
    <div class="rev-stars">★★★★★</div>
  </div>
  <div class="card review" style="left:295px;top:360px">
    <div class="avatar" role="img" aria-label="Customer photo"></div>
    <div class="rev-name">Paula S</div><div class="rev-role">Client</div>
    <p class="rev-text">I really wanted a house phone but I could not connect out here in the country. I called Harborline Telecom and now I have GREAT service. The best landline service by far!</p>
    <div class="rev-stars">★★★★★</div>
  </div>
</section>

</body>
</html>
```